Kelvane Plumbing Business cards

Company is Kelvane Plumbing.
name Dashel Morrowby, I am a plumber, drainer, gasfitter and roofer
Mobile: 0431 906 154
Email address: info@kelvaneplumbing.example (check out my website for some ideas)
Website: www.kelvaneplumbing.example
ABN: 82 916 203 471
LIC: 604517K

I am reliable all round plumber. I am a 24 hour emergency service. Kelvane Plumbing is a professional plumbing service in the Illawarra, South Coast, Southern Sydney and Southern Highland regions of NSW. We offer a 24 hour emergency service for piece of mind to our customers. Call us now to see how we can help you. Kelvane Plumbing approaches every job with attention to detail and excellent customer service. With our superior workmanship you can be confident that the job will be done right the first time around. You can rest assured with results that are guaranteed to last.

Target Market(s)

the general public

Contact Information for Business Card

look up website for some ideas something with similar colours to logo and new modern and to catch the eye.

Colors
fdfdfd
ffffff
000000
7f7f7f
aaaaaa
33a6d7
0492cd

Requirements
Must have
• all contact details
• company- Kelvane Plumbing
• name- Dashel Morrowby
• number mobile- 0431 906 154
• Email address- info@kelvaneplumbing.example
• Website- www.kelvaneplumbing.example
• ABN- 82 916 203 471
• LIC- 604517K

```html
<!DOCTYPE html>
<html lang="en">
<head>
<meta charset="utf-8">
<title>Kelvane Plumbing – Business Cards</title>
<link href="https://fonts.googleapis.com/css2?family=Poppins:wght@400;500;600&display=swap" rel="stylesheet">
<style>
  :root {
    --page-bg: #f7f7f7;
    --brand-blue: #0499cb;
    --accent-blue: #0492cd;
    --text-grey: #7f7f7f;
    --card-white: #ffffff;
  }
  * { margin: 0; padding: 0; box-sizing: border-box; }
  html, body { width: 1200px; height: 1000px; overflow: hidden; }
  body {
    position: relative;
    background: var(--page-bg);
    font-family: "Poppins", sans-serif;
    color: var(--text-grey);
  }
  .card {
    position: absolute;
    box-shadow: 0 12px 30px rgba(0,0,0,0.18);
  }

  /* Front */
  .card-front {
    left: 257px; top: 89px; width: 686px; height: 391px;
    background: var(--brand-blue);
  }
  .front-wordmark {
    position: absolute;
    left: 40px; right: 40px; top: 0; bottom: 0;
    display: flex; align-items: center; justify-content: center; gap: 18px;
    padding-top: 60px;
    color: var(--card-white);
    font-weight: 600;
    font-size: 44px;
    letter-spacing: 2px;
    text-transform: uppercase;
    white-space: nowrap;
  }
  .front-wordmark .mark-dot {
    width: 28px; height: 28px; border-radius: 50%;
    background: var(--card-white);
    flex: none;
  }

  /* Back */
  .card-back {
    left: 253px; top: 519px; width: 690px; height: 393px;
    background: var(--card-white);
  }
  .back-brand {
    position: absolute;
    left: 0; right: 0; top: 48px;
    display: flex; flex-direction: column; align-items: center; gap: 26px;
  }
  .back-brand .mark-dot {
    width: 64px; height: 64px; border-radius: 50%;
    background: var(--accent-blue);
  }
  .back-wordmark {
    font-weight: 600;
    font-size: 34px;
    letter-spacing: 10px;
    color: var(--text-grey);
    text-transform: uppercase;
    white-space: nowrap;
  }
  .holder {
    position: absolute;
    right: 366px; top: 264px;
    text-align: right;
  }
  .holder-name {
    color: var(--accent-blue);
    font-weight: 500;
    font-size: 20px;
    line-height: 28px;
  }
  .holder-role {
    font-size: 16px;
    line-height: 20px;
  }
  .contacts {
    position: absolute;
    left: 372px; top: 242px;
    list-style: none;
  }
  .contacts li {
    display: flex; align-items: center; gap: 12px;
    height: 29px;
    font-size: 16px;
    white-space: nowrap;
  }
  .contacts svg { width: 21px; height: 21px; flex: none; fill: var(--accent-blue); }
  .contacts .hl { color: var(--accent-blue); }
  .divider {
    position: absolute;
    left: 24px; right: 26px; top: 337px;
    height: 1px; background: var(--accent-blue);
  }
  .credentials {
    position: absolute;
    left: 0; right: 0; top: 350px;
    text-align: center;
    font-size: 17px;
    white-space: nowrap;
  }
  .credentials .label { color: var(--accent-blue); font-weight: 500; }
  .credentials .sep { margin: 0 8px; }
</style>
</head>
<body>
  <section class="card card-front">
    <div class="front-wordmark"><span class="mark-dot"></span><span>Kelvane Plumbing</span></div>
  </section>

  <section class="card card-back">
    <div class="back-brand">
      <span class="mark-dot"></span>
      <div class="back-wordmark">Kelvane Plumbing</div>
    </div>

    <div class="holder">
      <p class="holder-name">Dashel Morrowby</p>
      <p class="holder-role">Founder</p>
    </div>

    <ul class="contacts">
      <li>
        <svg viewBox="0 0 24 24" aria-hidden="true"><path d="M6.6 10.8a15.1 15.1 0 0 0 6.6 6.6l2.2-2.2a1 1 0 0 1 1-.25 11.4 11.4 0 0 0 3.6.57 1 1 0 0 1 1 1V20a1 1 0 0 1-1 1A17 17 0 0 1 3 4a1 1 0 0 1 1-1h3.5a1 1 0 0 1 1 1c0 1.25.2 2.45.57 3.57a1 1 0 0 1-.25 1z"/></svg>
        <span>0431 - 906 - 154</span>
      </li>
      <li>
        <svg viewBox="0 0 24 24" aria-hidden="true"><path d="M2 5h20v2l-10 6L2 7z M2 9l10 6 10-6v10H2z"/></svg>
        <span>info@kelvaneplumbing.example</span>
      </li>
      <li>
        <svg viewBox="0 0 24 24" aria-hidden="true"><path d="M12 2a10 10 0 1 0 0 20 10 10 0 0 0 0-20zm0 2c1 0 2.2 1.8 2.7 5H9.3C9.8 5.8 11 4 12 4zM4.3 9h3c-.1.6-.1 1.3-.1 2s0 1.4.1 2h-3a8 8 0 0 1 0-4zm5 0h5.4c.1.6.1 1.3.1 2s0 1.4-.1 2H9.3c-.1-.6-.1-1.3-.1-2s0-1.4.1-2zm7.4 0h3a8 8 0 0 1 0 4h-3c.1-.6.1-1.3.1-2s0-1.4-.1-2zM9.3 15h5.4c-.5 3.2-1.7 5-2.7 5s-2.2-1.8-2.7-5z"/></svg>
        <span>www.<span class="hl">kelvaneplumbing</span>.example</span>
      </li>
    </ul>

    <div class="divider"></div>

    <p class="credentials">
      <span class="label">ABN -</span> 82 916 203 471<span class="sep">|</span><span class="label">24*7</span> Emergency Service<span class="sep">|</span><span class="label">LIC -</span> 604517K
    </p>
  </section>
</body>
</html>
```